E-mailer for Invitation to a Webinar - based on cricket theme

We are an e-learning development organization. We are conducting a webinar and want to send this flyer as a e-Mail Newsletter where we would like people to click on the Register button and reach our registration page & register for the webinar.
I am looking for an e-mailer to be sent to prospective customers to participate in a Webinar. The e-Mailer must be based on Cricket theme. It will have the following sections:
- One short paragraph 2-3 sentences about the webinar.
- One Heading and 5 bullet points about the webinar.
- Another subheading and 5 bullet points about the benefits of attending the webinar.
- 1 Paragraph (4-5 sentences) describing the profile of the presenter.
- Place to display the date, time and Link to register for the Webinar.
- Place to display a list of the designation of business executives who must attend the webinar (Who Can Attend)
- Place to announce a Sweepstake (Slate Mini tablet for one lucky registrant)
The target group is Senior Management HR Professionals in Australia & Newzealand.
Here is the text to be used in the webinar:
Webinar Title: mLearning Pavilion Webinar
Sub Title: Smash out googlies of mLearning and be a winner
Para 1: Converting your existing eLearning programs to mLearning has its own set of unpredictable challenges. Taking you on the batting front, Tavrel plans to showcase how to smash out the 20 googlies of this match.
Sub Heading 1: Common mLearning Googlies
Bulletpoints:
- Do I need to start from scratch?
- Is unification possible? Mobile with Web?
- Will it make it a hole in my pocket?
- Which is the right development tool for me?
- Can mLearning be equally effective?
Sub Heading 2: Key Takeaways-
- Transit to mLearning cost-effectively
- Strategies for unifying web and mobile learning
- Pros & Cons of various development tools
- Samples of effective mLearning modules
- Hottest trends of mLearning
The pitch is ready! Join us for this exciting match on May 10 @ 2 PM ADT. Register for the Webinar Now!
Webinar Presenter
Hi All, I am Meera Kothari, an eLearning enthusiast and I
believe in drafting innovating solutions to increase uptake
of virtual learning. ANZ has been our key geography since
2011 and the response has been awesome! Off lately, I
can see that most of the organizations are facing
challenges around re-purposing existing e-Courses for tab/mobile delivery, and I plan to present solutions to them in this session. Please feel free to share your thoughts/questions and I shall plan to address them for you. Connect to me at: e-mail address.
Date: 10 May 2013
Time: 2:00 PM ADT to 3:00 PM ADT
Duration: 1 Hour
Target Market(s)
Senior HR Professionals / Training professionals from Australia & Newzealand
Industry/Entity Type
Business
Requirements
Must have
- It must have strong call to action (Register Button) somewhere at Top/Mid/Bottom part of the flyer.
Please use a cricket player's silhouette/ Ilustration/ vector preferable on the top.
Please use cricket ground and cricket elements as theme.
Nice to have
- Must gel with the colour themes of our website - http://www.tv-learnwise.net

```html
<!DOCTYPE html>
<html lang="en">
<head>
<meta charset="utf-8">
<title>mLearning Pavilion Webinar</title>
<link href="https://fonts.googleapis.com/css2?family=Arimo:ital,wght@0,400;0,700;1,700&family=Didact+Gothic&display=swap" rel="stylesheet">
<style>
  :root {
    --orange: #f07a3a;
    --orange-deep: #e0602a;
    --orange-text: #e8621f;
    --tagline: #c9531f;
    --sky: #4aa8e2;
    --sky-deep: #2f8fd0;
    --navy: #1d5f95;
    --ink: #1c1c1c;
    --ink-soft: #2e2e2e;
    --presenter-blue: #1f6fb5;
    --paper: #f7f7f7;
    --backdrop: #d9d9d9;
    --white: #ffffff;
  }
  * { box-sizing: border-box; margin: 0; padding: 0; }
  html, body { width: 1057px; height: 1200px; overflow: hidden; background: var(--backdrop); }
  body { font-family: "Arimo", Arial, sans-serif; color: var(--ink); }

  .flyer { position: relative; width: 1057px; height: 1200px; background: var(--paper); overflow: hidden; }

  .title-band {
    height: 96px; background: var(--orange);
    display: flex; align-items: center; justify-content: center;
  }
  .title-band h1 {
    color: var(--white); font-weight: 700; font-size: 60px; letter-spacing: 0.5px;
    text-shadow: 2px 3px 3px rgba(0,0,0,0.35);
  }

  .intro { position: relative; background: var(--sky); height: 390px; padding-top: 20px; }
  .player-figure {
    position: absolute; left: 34px; top: 8px; width: 70px; height: 98px;
    background: linear-gradient(180deg, var(--navy), #174a73);
    border-radius: 35px 35px 6px 6px; opacity: 0.85;
  }
  .tagline {
    text-align: center; font-family: "Didact Gothic", Arial, sans-serif;
    color: var(--tagline); font-size: 31px; letter-spacing: 2.5px; line-height: 1.1;
  }
  .tagline-win {
    text-align: center; color: var(--white); font-weight: 700; font-style: italic;
    font-size: 37px; line-height: 1.15; margin-top: 2px;
  }
  .intro-copy {
    width: 920px; margin: 14px auto 0; text-align: center;
    font-size: 17.5px; line-height: 1.35; color: var(--ink);
  }

  .columns { display: flex; justify-content: space-between; margin-top: 18px; padding-right: 40px; }
  .column { width: 470px; }
  .column.right { width: 440px; margin-top: 22px; }
  .ribbon {
    display: inline-block; background: var(--orange-deep); color: var(--white);
    font-weight: 700; font-style: italic; font-size: 22px;
    padding: 9px 46px 9px 40px;
    clip-path: polygon(0 0, 94% 0, 100% 100%, 0 100%);
    text-shadow: 1px 1px 2px rgba(0,0,0,0.3);
  }
  .column.right .ribbon { padding-left: 22px; clip-path: polygon(0 0, 92% 0, 100% 100%, 3% 100%); }
  .points { list-style: none; margin-top: 14px; padding-left: 42px; }
  .column.right .points { padding-left: 0; }
  .points li {
    position: relative; padding-left: 22px; font-size: 17.5px; line-height: 1.38; color: var(--white);
  }
  .points li::before {
    content: ""; position: absolute; left: 0; top: 6px; width: 11px; height: 11px;
    background: var(--orange); border: 1px solid rgba(255,255,255,0.7);
  }

  .wave { position: absolute; left: 0; top: 450px; width: 1057px; height: 90px; }

  .match { position: absolute; left: 0; top: 548px; width: 1057px; padding: 0 50px; }
  .pitch-call { text-align: center; font-weight: 700; font-size: 23px; line-height: 1.5; color: var(--ink-soft); }
  .pitch-call em { color: var(--orange-text); }
  .section-heading {
    margin-top: 14px; color: var(--presenter-blue); font-weight: 700; font-style: italic; font-size: 21px;
  }
  .presenter-copy { margin-top: 5px; font-size: 15.5px; line-height: 1.4; text-align: justify; color: var(--ink); }

  .extras { display: flex; justify-content: space-between; margin-top: 6px; }
  .attendees { width: 560px; }
  .attendee-list {
    list-style: none; margin-top: 6px;
    display: grid; grid-template-columns: 1fr 1fr; column-gap: 20px;
  }
  .attendee-list li { position: relative; padding-left: 18px; font-size: 15.5px; line-height: 1.45; }
  .attendee-list li::before {
    content: ""; position: absolute; left: 0; top: 7px; width: 9px; height: 9px; background: var(--orange);
  }
  .sweepstake {
    width: 380px; margin-top: 14px; padding: 10px 16px;
    border: 2px dashed var(--orange-deep); border-radius: 10px; background: #fff3ea;
  }
  .sweepstake h3 { color: var(--orange-text); font-weight: 700; font-style: italic; font-size: 20px; }
  .sweepstake p { margin-top: 4px; font-size: 15.5px; line-height: 1.4; color: var(--ink); }

  .schedule { position: absolute; left: 50px; top: 888px; z-index: 2; }
  .schedule p { font-weight: 700; font-size: 25px; line-height: 1.35; color: var(--ink); }
  .schedule span { color: var(--orange-text); font-style: italic; }

  .register {
    position: absolute; left: 775px; top: 878px; width: 245px; height: 150px; z-index: 2;
    background: linear-gradient(#f58a48, var(--orange-deep));
    border: 3px solid #f6a06b; border-radius: 24px;
    box-shadow: 0 6px 10px rgba(0,0,0,0.35);
    display: flex; flex-direction: column; align-items: center; justify-content: center;
    text-decoration: none; font-weight: 700; font-style: italic; line-height: 1;
  }
  .register .word { color: var(--white); font-size: 52px; text-shadow: 2px 2px 3px rgba(0,0,0,0.35); }
  .register .now { color: var(--sky-deep); font-size: 50px; margin-top: 4px; text-shadow: 1px 1px 0 rgba(255,255,255,0.6); }

  .ground {
    position: absolute; left: 0; top: 940px; width: 1057px; height: 260px;
    background:
      linear-gradient(to bottom, rgba(247,247,247,1) 0%, rgba(247,247,247,0) 22%),
      linear-gradient(to bottom, #8a8f99 22%, #6f6a6a 34%, #4f8a3a 40%, #5f9b3f 70%, #3f5e33 88%, #2a2a2a 100%);
  }
</style>
</head>
<body>
<main class="flyer">
  <header class="title-band">
    <h1>mLearning Pavilion Webinar</h1>
  </header>

  <section class="intro">
    <div class="player-figure" role="img" aria-label="Silhouette of a cricket batsman playing a shot"></div>
    <p class="tagline">Smash out googlies of mLearning</p>
    <p class="tagline-win">and be a winner</p>
    <p class="intro-copy">Converting your existing eLearning programs to mLearning has its own set of unpredictable challenges. Taking you on the batting front, Tavrel plans to showcase how to smash out the 20 googlies of this match.</p>

    <div class="columns">
      <div class="column left">
        <h2 class="ribbon">Common mLearning Googlies</h2>
        <ul class="points">
          <li>Do I need to start from scratch?</li>
          <li>Is unification possible? Mobile with Web?</li>
          <li>Will it make it a hole in my pocket?</li>
          <li>Which is the right development tool for me?</li>
          <li>Can mLearning be equally effective?</li>
        </ul>
      </div>
      <div class="column right">
        <h2 class="ribbon">Key Take aways</h2>
        <ul class="points">
          <li>Transit to mLearning cost-effectively</li>
          <li>Strategies for unifying web and mobile learning</li>
          <li>Pros &amp; Cons of various development tools</li>
          <li>Samples of effective mLearning modules</li>
          <li>Hottest trends of mLearning</li>
        </ul>
      </div>
    </div>
  </section>

  <svg class="wave" viewBox="0 0 1057 90" preserveAspectRatio="none" aria-hidden="true">
    <path d="M0 0 H1057 V30 C800 75 400 10 0 55 Z" fill="#4aa8e2"/>
    <path d="M0 55 C400 10 800 75 1057 30 V48 C800 88 420 30 0 70 Z" fill="#3a3a3a" opacity="0.75"/>
    <path d="M0 70 C420 30 800 88 1057 48 V90 H0 Z" fill="#f7f7f7"/>
  </svg>

  <section class="match">
    <p class="pitch-call">The pitch is ready! Join us for this exciting match <em>on May 10 @ 2 PM ADT.</em><br>Register for the Webinar Now!</p>
    <h3 class="section-heading">Webinar Presenter</h3>
    <p class="presenter-copy">Hi All, I am Meera Kothari, an eLearning enthusiast and I believe in drafting innovating solutions to increase uptake of virtual learning. ANZ has been our key geography since 2011 and the response has been awesome! Off lately, I can see that most of the organizations are facing challenges around re-purposing existing e-Courses for tab/mobile delivery, and I plan to present solutions to them in this session. Please feel free to share your thoughts/questions and I shall plan to address them for you. Connect to me at: e-mail address.</p>

    <div class="extras">
      <div class="attendees">
        <h3 class="section-heading">Who Can Attend</h3>
        <ul class="attendee-list">
          <li>HR Directors &amp; CHROs</li>
          <li>Chief Learning Officers</li>
          <li>Heads of Learning &amp; Development</li>
          <li>Training Managers</li>
          <li>Talent Development Leads</li>
          <li>eLearning Project Managers</li>
        </ul>
      </div>
      <aside class="sweepstake">
        <h3>Sweepstake!</h3>
        <p>Register now &ndash; one lucky registrant wins a Slate Mini tablet.</p>
      </aside>
    </div>
  </section>

  <div class="ground" role="img" aria-label="Photograph of a packed stadium overlooking a green striped playing field"></div>

  <div class="schedule">
    <p>Date: <span>10 May 2013</span></p>
    <p>Time: <span>2:00 PM ADT to 3:00 PM ADT</span></p>
    <p>Duration: <span>1 Hour</span></p>
  </div>

  <a class="register" href="#register">
    <span class="word">Register</span>
    <span class="now">Now</span>
  </a>
</main>
</body>
</html>
```